Business Card - Rebranding for Consulting Firm

We are renaming and rebranding our consulting firm and need to raise the level of quality of our cards as part of that effort. We consult to leading high tech, life science and other innovation sector companies.

Need a two-sided business card design.

Side 1: (a) Company logo (b) tag line: Optimize Your Investment in Talent (c) Name (d) Title (e) Phone 1: Office (f) Phone 2: Mobile (g) email: person@HollowmereAdvisory.com

Side 2: Two lines of text: (a) Vision is Essential. Markets Keep Moving. People Deliver Results. (b) We help you master all three.

Target Market(s)

Business and human resources executives and senior managers

Industry/Entity Type

Management Consulting

Contact Information for Business Card

Font styles to use
Sans Serif

Requirements
Must have
• clean, not too busy, but with a bit of creativity. Stick to the colors used in the attached logo
• appeal to high tech, life science companies
Nice to have
• prefer white background

```html
<!DOCTYPE html>
<html lang="en">
<head>
<meta charset="utf-8">
<title>Hollowmere Advisory – Business Card</title>
<link rel="stylesheet" href="https://fonts.googleapis.com/css2?family=Arimo:wght@400;700&display=swap">
<style>
  :root {
    --stage: #2a2a2b;
    --brand-blue: #1b75b0;
    --brand-blue-dark: #0f5d93;
    --navy: #123f72;
    --ink-grey: #4a4d52;
    --stripe-grey: #7d8187;
    --card-white: #f4f5f6;
    --white: #ffffff;
  }
  * { box-sizing: border-box; margin: 0; padding: 0; }
  html, body { width: 1200px; height: 997px; overflow: hidden; }
  body {
    background: var(--stage);
    font-family: "Arimo", Arial, sans-serif;
    position: relative;
  }
  .card {
    position: absolute;
    top: 340px;
    width: 525px;
    height: 300px;
    border-radius: 16px;
    overflow: hidden;
  }

  /* Back side */
  .card-back {
    left: 60px;
    background: linear-gradient(135deg, #2184bf 0%, var(--brand-blue) 55%, var(--brand-blue-dark) 100%);
    color: var(--white);
  }
  .card-back .wordmark {
    position: absolute;
    left: 0; right: 0; top: 96px;
    text-align: center;
    font-size: 46px;
    font-weight: 700;
    letter-spacing: -0.5px;
    color: var(--white);
  }
  .card-back .tagline {
    position: absolute;
    left: 0; right: 0; bottom: 46px;
    text-align: center;
    font-size: 12.5px;
    line-height: 1.5;
    color: #e6f1f9;
  }

  /* Front side */
  .card-front {
    left: 615px;
    background: linear-gradient(160deg, var(--white) 0%, var(--card-white) 100%);
  }
  .card-front .wordmark {
    position: absolute;
    right: 38px; top: 58px;
    font-size: 32px;
    font-weight: 700;
    letter-spacing: -0.5px;
    color: var(--navy);
  }
  .card-front .rule {
    position: absolute;
    left: 38px; right: 38px; top: 116px;
    height: 2px;
    background: var(--navy);
  }
  .card-front .person {
    position: absolute;
    left: 38px; top: 136px;
    width: 230px;
    border-bottom: 2px solid var(--navy);
    padding-bottom: 6px;
  }
  .person .name {
    font-size: 17px;
    font-weight: 700;
    color: var(--navy);
    letter-spacing: 0.3px;
  }
  .person .title {
    font-size: 13px;
    color: var(--ink-grey);
    margin-top: 2px;
  }
  .contacts {
    position: absolute;
    left: 38px; top: 196px;
    list-style: none;
  }
  .contacts li {
    display: flex;
    align-items: center;
    gap: 10px;
    font-size: 13.5px;
    color: var(--ink-grey);
    height: 20px;
  }
  .contacts svg { width: 15px; height: 15px; flex: none; }
  .card-front .bands {
    position: absolute;
    left: 0; bottom: 0;
    width: 525px; height: 60px;
  }
  .card-front .website {
    position: absolute;
    right: 24px; bottom: 17px;
    font-size: 13px;
    color: var(--white);
  }
</style>
</head>
<body>

  <section class="card card-back" aria-label="Card back">
    <div class="wordmark">Hollowmere Advisory</div>
    <p class="tagline">Vision is Essential. Markets Keep Moving. People Deliver Results.<br>We help you master all three.</p>
  </section>

  <section class="card card-front" aria-label="Card front">
    <div class="wordmark">Hollowmere Advisory</div>
    <div class="rule"></div>

    <div class="person">
      <div class="name">MARCUS HALE</div>
      <div class="title">Marketing Director</div>
    </div>

    <ul class="contacts">
      <li>
        <svg viewBox="0 0 16 16" aria-hidden="true"><circle cx="8" cy="8" r="8" fill="var(--brand-blue)"/><path d="M4 6.5c0-1 1.5-1.8 4-1.8s4 .8 4 1.8v.6H10.3v-.8H5.7v.8H4zM5 8h6l.6 3.5H4.4z" fill="#fff"/></svg>
        (555) 014-2281
      </li>
      <li>
        <svg viewBox="0 0 16 16" aria-hidden="true"><circle cx="8" cy="8" r="8" fill="var(--brand-blue)"/><rect x="5.5" y="3.5" width="5" height="9" rx="1" fill="#fff"/><rect x="6.5" y="5" width="3" height="5" fill="var(--brand-blue)"/></svg>
        (555) 017-3490
      </li>
      <li>
        <svg viewBox="0 0 16 16" aria-hidden="true"><circle cx="8" cy="8" r="8" fill="var(--brand-blue)"/><rect x="4" y="5" width="8" height="6" rx="0.6" fill="#fff"/><path d="M4.3 5.4 8 8.4l3.7-3" stroke="var(--brand-blue)" stroke-width="0.9" fill="none"/></svg>
        person@HollowmereAdvisory.com
      </li>
    </ul>

    <svg class="bands" viewBox="0 0 525 60" aria-hidden="true">
      <polygon points="0,38 300,38 310,30 525,30 525,34 312,34 302,46 0,46" fill="var(--stripe-grey)"/>
      <polygon points="0,50 305,50 322,24 525,24 525,60 0,60" fill="var(--brand-blue)"/>
    </svg>
    <div class="website">www.hollowmereadvisory.com</div>
  </section>

</body>
</html>
```